Stationary Design for Norvath Digital

We are after a full stationary back business cards, letterheads, compliment slip, invoice template, delivery note and anything else we could use within the stationary pack.

We would also like an email footer creating.

Our company details to be included on all stationary:

Registered Name: Norvath Limited
Company Registration Number: 20473915
Website: www.norvathdigital.example
email: info@norvathdigital.example
Phone: 01632 960 417
Address: 48 Tamsin Lane Loughborough Leicestershire United Kingdom LE11 9QX

```html
<!DOCTYPE html>
<html lang="en">
<head>
<meta charset="utf-8">
<title>Norvath Digital – Business Card</title>
<link rel="stylesheet" href="https://fonts.googleapis.com/css2?family=Michroma&family=Mulish:wght@300;400;600&display=swap">
<style>
  :root {
    --page-bg: #e9eaec;
    --navy-deep: #0f1a33;
    --navy-mid: #1e2f57;
    --navy-light: #34497a;
    --frost-light: #eef1f4;
    --frost-mid: #d9dee5;
    --text-light: #f1f3f7;
    --text-soft: #c9d0de;
    --brand-ink: #1b2745;
  }
  * { margin: 0; padding: 0; box-sizing: border-box; }
  html, body {
    width: 1200px; height: 969px; overflow: hidden;
    background: var(--page-bg);
  }
  .business-card {
    position: absolute; left: 100px; top: 201px;
    width: 1000px; height: 567px;
    background: linear-gradient(135deg, var(--frost-light), var(--frost-mid));
    box-shadow: 0 12px 40px rgba(15, 26, 51, 0.18);
    overflow: hidden;
  }
  .card-shape { position: absolute; inset: 0; width: 100%; height: 100%; }
  .contact-block {
    position: absolute; left: 52px; top: 76px;
    color: var(--text-light);
    font-family: "Mulish", sans-serif;
    font-weight: 300;
  }
  .person-name {
    font-family: "Michroma", sans-serif;
    font-size: 27px; letter-spacing: 0.5px;
    color: var(--text-soft);
  }
  .person-role {
    font-size: 23px; margin-top: 6px; color: var(--text-soft);
    letter-spacing: 0.5px;
  }
  .company-name {
    font-size: 25px; font-weight: 600; margin-top: 36px;
  }
  .company-address { font-size: 24.5px; line-height: 33px; letter-spacing: 0.5px; }
  .company-reg { font-size: 24.5px; margin-top: 2px; letter-spacing: 0.5px; }
  .contact-list { list-style: none; margin-top: 26px; }
  .contact-list li {
    display: flex; align-items: center; gap: 14px;
    color: var(--text-soft); font-size: 23px; height: 39px;
  }
  .contact-list li.phone { font-size: 27px; color: var(--text-light); }
  .contact-list svg { width: 22px; height: 22px; fill: var(--text-soft); flex: none; }
  .brand-name {
    position: absolute; left: 560px; top: 258px; width: 400px;
    text-align: center;
    font-family: "Michroma", sans-serif;
    font-size: 36px; color: var(--brand-ink);
    letter-spacing: 2px;
  }
</style>
</head>
<body>
  <div class="business-card">
    <svg class="card-shape" viewBox="0 0 1000 567" preserveAspectRatio="none" aria-hidden="true">
      <defs>
        <linearGradient id="panelFill" x1="0" y1="0" x2="1" y2="0.4">
          <stop offset="0" stop-color="var(--navy-light)"/>
          <stop offset="0.45" stop-color="var(--navy-mid)"/>
          <stop offset="1" stop-color="var(--navy-deep)"/>
        </linearGradient>
      </defs>
      <path class="navy-panel" d="M0 0 H485 C440 90 430 200 470 300 C510 390 545 470 480 567 H0 Z" fill="url(#panelFill)"/>
      <path class="accent-swoosh" d="M505 0 C455 90 445 200 487 300 C527 390 560 470 497 567 L509 567 C578 470 543 388 501 298 C462 200 472 90 521 0 Z" fill="var(--navy-deep)"/>
    </svg>

    <div class="contact-block">
      <p class="person-name">DANIEL HARTLEY</p>
      <p class="person-role">CEO/FOUNDER</p>
      <p class="company-name">Norvath Limited</p>
      <p class="company-address">48 Tamsin Lane Loughborough<br>Leicestershire<br>United Kingdom LE11 9QX</p>
      <p class="company-reg">Reg. No: 20473915</p>
      <ul class="contact-list">
        <li class="phone">
          <svg viewBox="0 0 24 24"><path d="M6.6 10.8a15.1 15.1 0 0 0 6.6 6.6l2.2-2.2a1 1 0 0 1 1-.25 11.4 11.4 0 0 0 3.6.57 1 1 0 0 1 1 1V20a1 1 0 0 1-1 1A17 17 0 0 1 3 4a1 1 0 0 1 1-1h3.5a1 1 0 0 1 1 1c0 1.25.2 2.45.57 3.57a1 1 0 0 1-.25 1z"/></svg>
          01632 960 417
        </li>
        <li class="email">
          <svg viewBox="0 0 24 24"><path d="M2 5h20v14H2z M4 7v.3l8 5 8-5V7l-8 5z" fill-rule="evenodd"/></svg>
          info@norvathdigital.example
        </li>
        <li class="web">
          <svg viewBox="0 0 24 24"><path d="M12 2a10 10 0 1 0 0 20 10 10 0 0 0 0-20zm6.9 6h-3a15.6 15.6 0 0 0-1.4-3.6A8 8 0 0 1 18.9 8zM12 4a14 14 0 0 1 1.9 4h-3.8A14 14 0 0 1 12 4zM4.3 14a8.2 8.2 0 0 1 0-4h3.4a16.5 16.5 0 0 0 0 4zm.8 2h3a15.6 15.6 0 0 0 1.4 3.6A8 8 0 0 1 5.1 16zm3-8h-3a8 8 0 0 1 4.4-3.6A15.6 15.6 0 0 0 8.1 8zM12 20a14 14 0 0 1-1.9-4h3.8A14 14 0 0 1 12 20zm2.3-6H9.7a14.7 14.7 0 0 1 0-4h4.6a14.7 14.7 0 0 1 0 4zm.2 5.6a15.6 15.6 0 0 0 1.4-3.6h3a8 8 0 0 1-4.4 3.6zm1.8-5.6a16.5 16.5 0 0 0 0-4h3.4a8.2 8.2 0 0 1 0 4z"/></svg>
          www.norvathdigital.example
        </li>
      </ul>
    </div>

    <p class="brand-name">NORVATH DIGITAL</p>
  </div>
</body>
</html>
```